Lumo4Kart - a fintech company - business card

We need a business card design for our Payments Technology company in Sydney, Australia. We provide business with payment solutions expanding across EFTPOS machines, online payment gateways and mobile payment solutions. We would like to see designs that are clean, classy and professional.
Target Market(s)
Business professionals, executives, c-suite
Industry/Entity Type
Fintech
Contact Information for Business Card
Will be on 400gsm. Logo will most likely be spot gloss unless designer recommends otherwise.
Font styles to use
Sans Serif
Requirements
Must have
- We need our website (lumo4kart.com.au), email (contact@lumo4kart.com.au), mobile (0432 587 904) and direct phone number (02 6815 3927) to feature on the card along with our logo (attached) and the words "EFTPOS | ONLINE | MOBILE"
- Font = Roboto

```html
<!DOCTYPE html>
<html lang="en">
<head>
<meta charset="utf-8">
<title>Lumo4Kart business card</title>
<link rel="stylesheet" href="https://fonts.googleapis.com/css2?family=Roboto:wght@300;400;900&display=swap">
<style>
  :root {
    --stage: #3b3e43;
    --card: #1c1d20;
    --brand-blue: #2f7dc0;
    --brand-grey: #7f8083;
    --text-grey: #9a9b9e;
    --name-grey: #a9aaac;
  }
  * { margin: 0; padding: 0; box-sizing: border-box; }
  html, body { width: 1200px; height: 900px; overflow: hidden; }
  body {
    background: var(--stage);
    font-family: "Roboto", Arial, sans-serif;
    display: flex;
    align-items: center;
    justify-content: center;
    gap: 40px;
  }
  .card {
    position: relative;
    width: 540px;
    height: 309px;
    background: var(--card);
    border-radius: 24px;
    overflow: hidden;
    box-shadow: 0 14px 30px rgba(0,0,0,0.35);
  }
  .wordmark {
    display: flex;
    align-items: center;
    gap: 14px;
  }
  .wordmark__name {
    font-weight: 900;
    color: var(--brand-grey);
    letter-spacing: 0.5px;
    text-transform: uppercase;
    white-space: nowrap;
  }
  .wordmark__dot {
    border-radius: 50%;
    background: var(--brand-blue);
    flex: none;
  }

  /* contact side */
  .card--contact .wordmark {
    position: absolute;
    left: 44px;
    top: 48px;
  }
  .card--contact .wordmark__name { font-size: 36px; }
  .card--contact .wordmark__dot { width: 58px; height: 58px; }
  .contact {
    position: absolute;
    left: 262px;
    top: 146px;
  }
  .contact__name {
    font-size: 25px;
    font-weight: 300;
    color: var(--name-grey);
    letter-spacing: 1px;
    text-transform: uppercase;
  }
  .contact__role {
    font-size: 13px;
    color: var(--brand-blue);
    margin: 2px 0 12px;
  }
  .contact__list { list-style: none; }
  .contact__item {
    display: flex;
    align-items: center;
    gap: 9px;
    font-size: 13.5px;
    color: var(--text-grey);
    line-height: 21px;
  }
  .contact__icon { width: 12px; height: 12px; flex: none; }

  /* front side */
  .card--front .accent {
    position: absolute;
    left: -120px;
    top: -180px;
    width: 360px;
    height: 360px;
    border-radius: 50%;
    background: var(--brand-blue);
  }
  .card--front .brand-block {
    position: absolute;
    right: 40px;
    bottom: 44px;
    text-align: right;
  }
  .card--front .wordmark__name { font-size: 36px; }
  .card--front .wordmark__dot { width: 64px; height: 64px; }
  .tagline {
    margin-top: 8px;
    font-size: 13px;
    font-weight: 400;
    color: var(--text-grey);
    letter-spacing: 1.2px;
    padding-right: 78px;
  }
</style>
</head>
<body>

  <section class="card card--contact">
    <div class="wordmark">
      <span class="wordmark__name">Lumo4Kart</span>
      <span class="wordmark__dot"></span>
    </div>

    <div class="contact">
      <p class="contact__name">Your Name</p>
      <p class="contact__role">Job Title</p>
      <ul class="contact__list">
        <li class="contact__item">
          <svg class="contact__icon" viewBox="0 0 12 12"><rect x="3" y="0.5" width="6" height="11" rx="1.2" fill="none" stroke="var(--brand-blue)" stroke-width="1.2"/><circle cx="6" cy="9.5" r="0.8" fill="var(--brand-blue)"/></svg>
          0432 587 904
        </li>
        <li class="contact__item">
          <svg class="contact__icon" viewBox="0 0 12 12"><path d="M1 4 Q6 0 11 4 L10 5.5 L8 4.8 L8 3.8 Q6 3 4 3.8 L4 4.8 L2 5.5 Z" fill="var(--brand-blue)"/><rect x="2" y="6" width="8" height="5.5" rx="1" fill="var(--brand-blue)"/><circle cx="6" cy="8.7" r="1.4" fill="var(--card)"/></svg>
          02 6815 3927
        </li>
        <li class="contact__item">
          <svg class="contact__icon" viewBox="0 0 12 12"><rect x="0.5" y="2" width="11" height="8" rx="1" fill="var(--brand-blue)"/><path d="M1 2.8 L6 6.8 L11 2.8" fill="none" stroke="var(--card)" stroke-width="1"/></svg>
          contact@lumo4kart.com.au
        </li>
        <li class="contact__item">
          <svg class="contact__icon" viewBox="0 0 12 12"><circle cx="6" cy="6" r="5.2" fill="none" stroke="var(--brand-blue)" stroke-width="1.2"/><ellipse cx="6" cy="6" rx="2.2" ry="5.2" fill="none" stroke="var(--brand-blue)" stroke-width="1"/><line x1="0.8" y1="6" x2="11.2" y2="6" stroke="var(--brand-blue)" stroke-width="1"/></svg>
          lumo4kart.com.au
        </li>
      </ul>
    </div>
  </section>

  <section class="card card--front">
    <span class="accent"></span>
    <div class="brand-block">
      <div class="wordmark">
        <span class="wordmark__name">Lumo4Kart</span>
        <span class="wordmark__dot"></span>
      </div>
      <p class="tagline">EFTPOS | ONLINE | MOBILE</p>
    </div>
  </section>

</body>
</html>
```